Hollowmere Dental Center Specials/Offers

Take the advertisement pic (LABELED ADVERTISEMENT) and make it look "professional in appearance" using the logo and color scheme of Hollowmere Dental Center. The Phone number should be 719-555-0186. I want the same content, different background, professional looking document. I want it to be a 12"x12" document. High resolution files should include .PDF, .JPG and .AI. Any or all documents can be used for colors and overall scheme. I would like to have the overall colors include the main blue color from the file 4db749b4ef4c5e0717512bf7eb26bf54 and include the brown "swoosh" somewhere through/on the final document. Stock files of smiling young families can be used but not required. I am on a tight time-line and have placed 5 days as the deadline, but I will pick my favorite in as little as 2-3 days if I can get a good product. Again ALL the info from the Advertisement document should be included on the final product. Use any or all of the uploaded files for assistance. You can also visit our website for more info: www.hollowmeredentalcenter.example Thanks

```html
<!DOCTYPE html>
<html lang="en">
<head>
<meta charset="utf-8">
<title>Hollowmere Dental Center – Specials &amp; Offers</title>
<link rel="stylesheet" href="https://fonts.googleapis.com/css2?family=Roboto:wght@300;400;500;700;900&family=Roboto+Condensed:wght@700&display=swap">
<style>
  :root {
    --white: #ffffff;
    --ink: #1e1e20;
    --panel-grey: #4b4b4d;
    --band-teal: #5f93a0;
    --badge-teal: #4aacb8;
    --badge-muted: #6a97a3;
    --accent-teal: #33b6ae;
    --link-teal: #4f8e9c;
    --brand-brown: #5b4a44;
    --soft-grey: #5a5a5c;
  }
  * { box-sizing: border-box; margin: 0; padding: 0; }
  html, body { width: 1200px; height: 1200px; overflow: hidden; background: var(--white); }
  body { font-family: "Roboto", Arial, sans-serif; color: var(--ink); }

  .ad { position: relative; width: 1200px; height: 1200px; background: var(--white); overflow: hidden; }

  .family-photo {
    position: absolute; left: 384px; top: 0; width: 816px; height: 720px;
    background:
      linear-gradient(90deg, var(--white) 0%, rgba(255,255,255,0) 14%),
      radial-gradient(ellipse at 80% 20%, #cfe0a6 0%, rgba(207,224,166,0) 45%),
      radial-gradient(ellipse at 25% 55%, #f1e39a 0%, rgba(241,227,154,0) 50%),
      radial-gradient(ellipse at 75% 65%, #f3d9d2 0%, rgba(243,217,210,0) 50%),
      linear-gradient(160deg, #f4efd9 0%, #eadfc0 50%, #e9d3c8 100%);
  }

  .waves { position: absolute; left: 0; top: 0; width: 1200px; height: 1200px; }

  .brand { position: absolute; left: 40px; top: 92px; }
  .brand-name { display: flex; align-items: center; gap: 14px; }
  .brand-dot { width: 44px; height: 44px; border-radius: 50%; background: var(--badge-teal); }
  .brand-title { font-weight: 400; font-size: 31px; color: var(--brand-brown); line-height: 1.1; }
  .brand-tagline { margin-top: 12px; margin-left: 58px; font-size: 16px; letter-spacing: 1.5px; color: var(--soft-grey); }

  .headline { position: absolute; left: 66px; top: 388px; font-size: 80px; line-height: 80px; color: var(--ink); letter-spacing: -1px; }
  .headline .light { font-weight: 300; }
  .headline .heavy { font-weight: 900; }
  .headline .line { display: block; }

  .badge { position: absolute; border-radius: 50%; display: flex; flex-direction: column; align-items: center; justify-content: center; text-align: center; }
  .badge-whitening { left: 924px; top: 471px; width: 232px; height: 232px; background: var(--badge-teal); color: var(--white); }
  .badge-whitening .price { font-weight: 300; font-size: 90px; line-height: 90px; }
  .badge-whitening .label { font-family: "Roboto Condensed", Arial, sans-serif; font-weight: 700; font-size: 31px; line-height: 33px; margin-top: 6px; }

  .badge-discount { left: 62px; top: 793px; width: 364px; height: 364px; background: var(--badge-muted); color: var(--white); }
  .badge-discount .amount { font-weight: 300; font-size: 104px; line-height: 100px; letter-spacing: -2px; }
  .badge-discount .amount small { font-size: 46px; font-weight: 400; letter-spacing: 0; }
  .badge-discount .terms { font-family: "Roboto Condensed", Arial, sans-serif; font-weight: 700; font-size: 30px; line-height: 40px; margin-top: 12px; }
  .badge-discount .note { font-family: "Roboto Condensed", Arial, sans-serif; font-weight: 700; font-size: 20px; line-height: 26px; margin-top: 16px; }

  .badge-referral { left: 1000px; top: 891px; width: 162px; height: 162px; background: var(--white); color: var(--soft-grey); font-size: 20px; line-height: 26px; font-weight: 400; }

  .offer { position: absolute; left: 537px; color: var(--white); }
  .offer h2 { color: var(--accent-teal); font-weight: 400; }
  .offer p { font-size: 26px; line-height: 35px; }
  .offer .fine { font-size: 20px; line-height: 35px; }
  .offer-providers { top: 724px; }
  .offer-providers h2 { font-size: 28px; line-height: 36px; }
  .offer-new-patients { top: 902px; }
  .offer-new-patients h2 { font-size: 35px; line-height: 40px; }

  .contact { position: absolute; right: 48px; top: 1102px; text-align: center; }
  .contact .call { font-weight: 700; font-size: 27px; color: #3e3e40; }
  .contact .phone { font-weight: 700; font-size: 42px; color: var(--link-teal); margin-left: 6px; vertical-align: -3px; }
  .contact .web { display: block; font-weight: 700; font-size: 26px; color: var(--link-teal); margin-top: 2px; }
</style>
</head>
<body>
<main class="ad">
  <div class="family-photo" role="img" aria-label="Smiling young family: mother and father each carrying a laughing child piggyback outdoors"></div>

  <svg class="waves" viewBox="0 0 1200 1200" aria-hidden="true">
    <path d="M0 637 C 150 662, 280 700, 420 692 C 640 680, 900 630, 1200 606 L 1200 1200 L 0 1200 Z" fill="var(--band-teal)"/>
    <path d="M0 682 C 150 710, 290 736, 440 726 C 660 712, 920 664, 1200 620 L 1200 1083 L 0 1083 Z" fill="var(--panel-grey)"/>
    <rect x="0" y="1083" width="1200" height="117" fill="var(--white)"/>
  </svg>

  <header class="brand">
    <div class="brand-name">
      <span class="brand-dot"></span>
      <span class="brand-title">Hollowmere Dental Center</span>
    </div>
    <p class="brand-tagline">FAMILY • COSMETIC • IMPLANTS</p>
  </header>

  <h1 class="headline">
    <span class="line light">WHERE THE</span>
    <span class="line heavy">WHOLE FAMILY</span>
    <span class="line"><span class="heavy">CAN</span> <span class="light">BE SEEN!</span></span>
  </h1>

  <div class="badge badge-whitening">
    <span class="price">$99</span>
    <span class="label">Bleeching<br>Specials</span>
  </div>

  <section class="offer offer-providers">
    <h2>Preferred Provider For:</h2>
    <p>Delmar Dental, Meridia Life, Crestline, Avena Health<br>BR/BS and Unity Concordant</p>
    <p class="fine">We take all other non-HMO Plans</p>
  </section>

  <section class="offer offer-new-patients">
    <h2>$59 New patients X-Rays</h2>
    <p>Comprehensive Exam<br>Regular Cleaning</p>
    <p class="fine">*Only patients without Dental Benefits</p>
  </section>

  <div class="badge badge-referral">ASK<br>ABOUT OUR<br>REFERRAL<br>PROGRAM</div>

  <div class="badge badge-discount">
    <span class="amount">20%<small>OFF</small></span>
    <span class="terms">Treatment scheduled<br>on your first visit.</span>
    <span class="note">Only patients without<br>Dental Benefits</span>
  </div>

  <footer class="contact">
    <span class="call">Call Today for an Appointment</span><span class="phone">719-555-0186</span>
    <span class="web">www.hollowmeredentalcenter.example</span>
  </footer>
</main>
</body>
</html>
```